Business card and stationery for startup company
Marla Quenby & Associates
Business card and stationery for startup company - Corporate Services
Creative Brief
Professional
Marla Quenby
PO Box 382 Northville, MI 48193
marlaequenby@postvane.com
Concepts
Business Cards and Stationery for Background Check Company
Business Cards and Stationery for new compliance company.

```html
<!DOCTYPE html>
<html lang="en">
<head>
<meta charset="utf-8">
<title>Marla Quenby &amp; Associates — Business Card</title>
<link rel="stylesheet" href="https://fonts.googleapis.com/css2?family=Cinzel:wght@400;600&display=swap">
<style>
  :root {
    --page-bg: #e9e7e3;
    --card-white: #ffffff;
    --brand-navy: #1f2a5c;
    --brand-blue: #1b7cc1;
    --accent-brown: #5b2e14;
    --text-light: #ffffff;
  }
  html, body {
    margin: 0;
    width: 1200px;
    height: 804px;
    overflow: hidden;
    background: var(--page-bg);
  }
  .business-card {
    position: absolute;
    left: 100px;
    top: 122px;
    width: 1000px;
    height: 560px;
    border-radius: 28px;
    overflow: hidden;
    background: var(--card-white);
    box-shadow: 0 6px 18px rgba(0, 0, 0, 0.18);
    font-family: "Cinzel", "Times New Roman", serif;
  }
  .card-waves {
    position: absolute;
    inset: 0;
    width: 1000px;
    height: 560px;
  }
  .wave-accent { fill: var(--accent-brown); }
  .wave-band { fill: var(--brand-blue); }

  .brand-lockup {
    position: absolute;
    left: 96px;
    top: 92px;
    display: flex;
    align-items: center;
    gap: 22px;
  }
  .brand-mark {
    width: 78px;
    height: 78px;
    border-radius: 50%;
    background: var(--brand-blue);
    flex: none;
  }
  .brand-name {
    margin: 0;
    font-weight: 600;
    font-size: 38px;
    line-height: 1;
    color: var(--brand-navy);
    letter-spacing: 0.5px;
  }
  .brand-suffix {
    font-size: 22px;
  }
  .brand-tagline {
    margin: 10px 0 0 2px;
    font-weight: 400;
    font-size: 17px;
    letter-spacing: 0.6px;
    text-transform: uppercase;
    color: var(--brand-navy);
  }

  .person-name {
    position: absolute;
    left: 140px;
    top: 398px;
    margin: 0;
    font-weight: 400;
    font-size: 32px;
    color: var(--text-light);
    letter-spacing: 1px;
  }
  .divider {
    position: absolute;
    left: 490px;
    top: 362px;
    width: 1.5px;
    height: 150px;
    background: rgba(255, 255, 255, 0.85);
  }
  .contact-list {
    position: absolute;
    left: 528px;
    top: 356px;
    margin: 0;
    padding: 0;
    list-style: none;
    color: var(--text-light);
    font-size: 21px;
    line-height: 39px;
    letter-spacing: 0.4px;
  }
  .contact-list li {
    display: flex;
    align-items: center;
    gap: 8px;
  }
  .contact-email { text-transform: uppercase; }
  .contact-icon {
    width: 16px;
    height: 16px;
    fill: none;
    stroke: var(--text-light);
    stroke-width: 1.8;
    flex: none;
  }
</style>
</head>
<body>
  <article class="business-card">
    <svg class="card-waves" viewBox="0 0 1000 560" aria-hidden="true">
      <path class="wave-accent" d="M0,322 C260,262 620,246 1000,282 L1000,300 C620,268 260,286 0,338 Z"/>
      <path class="wave-band" d="M0,350 C260,296 620,282 1000,312 L1000,560 L0,560 Z"/>
    </svg>

    <header class="brand-lockup">
      <span class="brand-mark" aria-hidden="true"></span>
      <div class="brand-text">
        <h1 class="brand-name">Marla Quenby &amp; Associates, <span class="brand-suffix">LLC</span></h1>
        <p class="brand-tagline">Partners for compliance and workforce screening</p>
      </div>
    </header>

    <h2 class="person-name">Marla Quenby</h2>
    <div class="divider" aria-hidden="true"></div>

    <ul class="contact-list">
      <li>PO Box 382</li>
      <li>Ashbrook, MI 48193</li>
      <li>
        <svg class="contact-icon" viewBox="0 0 16 16" aria-hidden="true">
          <rect x="4" y="1.5" width="8" height="13" rx="1.5"/>
          <line x1="7" y1="12" x2="9" y2="12"/>
        </svg>
        555-214-0174
      </li>
      <li class="contact-email">
        <svg class="contact-icon" viewBox="0 0 16 16" aria-hidden="true">
          <rect x="1.5" y="3.5" width="13" height="9" rx="1"/>
          <polyline points="1.5,4 8,9 14.5,4"/>
        </svg>
        marlaequenby@postvane.com
      </li>
    </ul>
  </article>
</body>
</html>
```